New Dynamic Design Based on Other Site

We need a new website designed where the front page is VERY SEO Friendly. The front page should almost follow the same SEO principles that are on BrivoPageKit.com. The inner pages need to follow the same exact video animations that occur on vulmo.com. I'd like to keep our "quillbys" theme throughout the new design but we will provide all of the content but I want someone to design something SEO friendly, new blog theme, and actual inner pages that are dynamic and based on those short videos.

Check attached file for company name and site that we currently have. Feel free to pull the content from that site and re-use it and also leave placeholders for the rest of them.

PLEASE NO USE OF STOCK IMAGES. Use a designer or an illustrator to create the various images.
Updates

Please make sure the front page is SEO friendly! Make sure you familiarize yourself with the brintle algorithm for SEO. Content above the fold H1 Tags Very mobile friendly Minimal javascript and animations Basically a quality static page with optimized content

Reason: Still waiting on some more designs.

Target Market(s)

call center companies, anything call related

Industry/Entity Type

Telecommunications

Number of Pages Required

4 page

Font styles to use
Sans Serif

Colors
33a6d7
85cae6
0792cd
0255a3
cee9f5
ecf7fb
ffffff

Requirements
Must have
• places for video animations
• dynamic functionality
• SEO friendly (front page)
Should not have
• should not look like a template. needs to be unique

```html
<!DOCTYPE html>
<html lang="en">
<head>
<meta charset="utf-8">
<title>DialMetric — Call Quality Analytics</title>
<link rel="stylesheet" href="https://fonts.googleapis.com/css2?family=Montserrat:wght@400;600;700&family=Open+Sans:wght@400;600&display=swap">
<style>
:root{
  --blue:#0792cd; --blue-mid:#33a6d7; --blue-light:#85cae6; --blue-pale:#cee9f5; --blue-wash:#ecf7fb;
  --navy:#0b2d5a; --deep:#0255a3; --ink:#222831; --text:#6b7480; --grey:#f0f0f0; --footer:#2e3136; --white:#fff;
}
*{box-sizing:border-box;margin:0;padding:0}
html,body{width:1200px;height:3509px;overflow:hidden}
body{font-family:"Open Sans",Arial,sans-serif;color:var(--text);background:var(--white);font-size:14px}
h1,h2,h3,h4,.nav,.btn,.label{font-family:Montserrat,Arial,sans-serif}
section,header,footer{position:relative;width:1200px;overflow:hidden}

.topbar{height:28px;background:var(--navy);color:#cfd8e6;font-size:9px;display:flex;align-items:center;gap:40px;padding-left:234px;white-space:nowrap}
.topbar span{display:flex;align-items:center;gap:7px}
.topbar i{width:10px;height:10px;border:1.5px solid #cfd8e6;border-radius:50%;display:inline-block}

.mainnav{height:61px;display:flex;align-items:center;justify-content:space-between;padding:0 234px 0 230px;border-bottom:1px solid #eee}
.brand{display:flex;align-items:center;gap:8px;font-family:Montserrat,sans-serif;font-weight:600;font-size:21px;color:var(--ink);white-space:nowrap}
.brand .dot{width:24px;height:24px;border-radius:50%;background:var(--blue)}
.nav{display:flex;gap:20px;font-size:9px;font-weight:600;color:#5b6470;white-space:nowrap}
.nav .on{color:var(--blue);position:relative}
.nav .on:after{content:"";position:absolute;left:-10px;right:-10px;bottom:-26px;height:3px;background:var(--blue)}

.hero{height:442px;background:var(--blue);text-align:center;color:var(--white)}
.hero .kicker{font-family:Montserrat,sans-serif;font-weight:600;font-size:13px;letter-spacing:1.5px;margin-top:38px}
.hero h1{font-size:26px;font-weight:700;line-height:30px;margin-top:12px;letter-spacing:.5px}
.hero .device{position:absolute;left:234px;top:145px;width:732px;height:297px;background:#141a22;border-radius:14px 14px 0 0;padding:14px 14px 0}
.hero .screen{width:704px;height:283px;background:linear-gradient(180deg,#f6f8fa 0%,#eef3f8 45%,#c9d4ee 70%,#8a9ad8 100%)}

.features{height:292px;display:flex;justify-content:center;padding-top:58px}
.feature{width:245px;text-align:center;padding:0 16px;border-right:1px solid #e4e4e4}
.feature:last-child{border:0}
.feature h3{font-family:"Open Sans",sans-serif;font-weight:600;font-size:13px;color:var(--ink);margin:14px 0 10px}
.feature p{font-size:9.5px;line-height:15px}

.why{height:304px;background:var(--blue-wash)}
.why .art{position:absolute;left:234px;top:42px;width:370px;height:222px;background:radial-gradient(circle at 60% 45%,#e3eef5,#f3f8fb 70%)}
.why .laptop{position:absolute;left:295px;top:115px;width:220px;height:134px;background:var(--white);border:8px solid #1d2430;border-radius:6px}
.accordion{position:absolute;left:615px;top:48px;width:351px}
.acc-head{height:28px;background:var(--white);display:flex;align-items:center;justify-content:space-between;padding-left:12px;font-size:11px;color:#8a939d;margin-bottom:8px}
.acc-head.open{color:var(--ink);font-weight:600;margin-bottom:0}
.acc-head b{width:22px;height:22px;margin-right:4px;background:var(--navy);color:var(--white);display:flex;align-items:center;justify-content:center;font-size:16px}
.acc-body{background:var(--white);border-top:1px solid #eee;padding:10px 24px 12px;font-size:9px;line-height:14px;margin-bottom:8px}

.intro{height:190px;text-align:center}
.section-title{font-size:19px;font-weight:700;color:var(--ink);letter-spacing:.5px}
.intro .section-title{margin-top:60px}
.lead{width:430px;margin:18px auto 0;font-size:10px;line-height:16px}

.tiles{height:269px;display:flex}
.tile{width:300px;height:269px;display:flex;flex-direction:column;align-items:center;color:var(--white)}
.tile:nth-child(odd){background:var(--blue)}
.tile:nth-child(even){background:var(--blue-light)}
.tile svg{margin-top:70px;width:110px;height:100px}
.tile .label{margin-top:50px;font-size:9px;font-weight:700;letter-spacing:.5px}
.tile.pale svg{margin-top:60px}
.tile.pale .label{margin-top:60px}

.newsletter{height:65px;background:var(--navy);display:flex;align-items:center;justify-content:center;gap:40px;color:var(--white)}
.newsletter h4{font-size:11px;letter-spacing:1.5px}
.btn{display:inline-flex;align-items:center;justify-content:center;font-size:9px;font-weight:700;letter-spacing:.8px}
.newsletter .btn{width:150px;height:32px;background:var(--white);color:var(--ink)}

.pricing{height:637px;text-align:center}
.pricing .section-title{margin-top:72px}
.plans{position:absolute;top:215px;left:229px;display:flex;gap:25px;align-items:flex-start}
.plan{width:232px;height:340px;background:var(--blue-wash);position:relative}
.plan .ribbon{height:24px;background:var(--blue-light);color:var(--white);font-family:Montserrat,sans-serif;font-size:9px;font-weight:700;display:flex;align-items:center;justify-content:center;letter-spacing:1px}
.plan.featured{height:362px;margin-top:-14px}
.plan.featured .ribbon{height:26px;background:var(--navy)}
.price{margin:24px 0 0;font-family:Montserrat,sans-serif;font-size:34px;font-weight:600;color:var(--ink)}
.price sup{font-size:16px;vertical-align:14px}
.price small{font-size:8px;font-weight:600;margin-left:2px}
.bar{width:60px;height:6px;background:var(--blue-light);margin:-8px auto 26px}
.plan ul{list-style:none;font-size:9.5px;line-height:22px}
.plan .btn{margin-top:30px;width:122px;height:24px;border:1px solid #cfd6dc;color:#555;background:var(--white)}
.plan.featured .btn{border:0;background:var(--blue);color:var(--white)}

.video{height:362px;display:flex}
.video .copy{width:600px;background:var(--grey);padding:60px 0 0 230px}
.video .copy h2{font-size:18px;color:var(--ink)}
.video .copy p{width:320px;font-size:10px;line-height:17px;margin-top:24px}
.video .copy .btn{margin-top:22px;width:215px;height:34px;background:var(--blue-mid);color:var(--white)}
.video .player{width:600px;background:var(--blue-mid);position:relative}
.video .screen{position:absolute;left:130px;top:78px;width:340px;height:214px;background:linear-gradient(#6ec0e6,#4fb1df);border-radius:8px}
.video .play{position:absolute;left:279px;top:163px;width:44px;height:44px;border:3px solid var(--white);border-radius:50%}
.video .play:after{content:"";position:absolute;left:14px;top:9px;border-left:16px solid var(--white);border-top:10px solid transparent;border-bottom:10px solid transparent}

.team{height:554px;text-align:center}
.team .section-title{margin-top:66px}
.members{position:absolute;top:187px;left:229px;display:flex;gap:24px}
.member{width:230px}
.member .photo{height:241px;background:linear-gradient(160deg,#c9cdd2,#eceef0)}
.member.active .photo{background:linear-gradient(160deg,#5fb6e2,#2f9fd4);display:flex;align-items:center;justify-content:center;gap:4px}
.member.active .photo i{width:18px;height:18px;background:var(--white);opacity:.9;margin-top:40px}
.member h4{font-family:"Open Sans",sans-serif;font-size:12px;font-weight:600;color:var(--ink);margin-top:18px}
.member span{font-size:8px;letter-spacing:.5px}
.arrow{position:absolute;top:298px;width:22px;height:22px;border-radius:50%;border:1px solid #ddd;background:var(--white)}

.site-footer{height:305px;background:var(--footer);color:#b9bec6}
.site-footer .brand{position:absolute;left:232px;top:62px;color:var(--white)}
.contact{position:absolute;left:232px;top:172px;font-size:9.5px;line-height:18px;list-style:none}
.fcol{position:absolute;top:60px}
.fcol h4{font-size:9px;color:var(--white);letter-spacing:1px;padding-bottom:8px;border-bottom:1px solid #474b52;width:250px}
.links{list-style:none;font-size:9.5px;line-height:28px}
.links li:before{content:"›";margin-right:8px}
.post{display:flex;gap:12px;margin-top:16px;width:250px}
.post i{width:40px;height:40px;background:#4a4e55;flex:none}
.post b{display:block;font-family:Montserrat,sans-serif;font-size:8px;color:var(--white);line-height:12px}
.post small{font-size:8px}
.copyright{position:absolute;left:0;right:0;bottom:0;height:28px;border-top:1px solid #3b3f45;font-size:8px;display:flex;align-items:center;justify-content:space-between;padding:0 232px}
.copyright span i{display:inline-block;width:8px;height:8px;background:#8d939b;margin-left:10px}
</style>
</head>
<body>

<header>
  <div class="topbar"><span><i></i>SUPPORT@DIALMETRIC.COM</span><span><i></i>PHONE +1 (555) 010-2040</span></div>
  <nav class="mainnav">
    <div class="brand"><span class="dot"></span>DialMetric</div>
    <div class="nav"><span class="on">HOME</span><span>SERVICES</span><span>SYSTEM DETAILS</span><span>SAMPLE SCORECARDS</span><span>PRICING</span><span>TEAM</span><span>BLOG</span><span>CONTACT US</span></div>
  </nav>
</header>

<section class="hero">
  <p class="kicker">HELLO, ARE YOU READY TO START ?</p>
  <h1>LOREM &amp; DOLOR<br>SIT AMET NONUMMY</h1>
  <div class="device">
    <div class="screen" role="img" aria-label="Product screenshot of the call analytics dashboard"></div>
  </div>
</section>

<section class="features">
  <div class="feature">
    <svg width="38" height="34" viewBox="0 0 38 34" fill="none" stroke="var(--blue)" stroke-width="2"><rect x="4" y="16" width="6" height="14"/><rect x="13" y="8" width="6" height="22"/><rect x="22" y="12" width="6" height="18"/><rect x="31" y="4" width="4" height="26"/><line x1="1" y1="32" x2="37" y2="32"/></svg>
    <h3>Dolore magna aliquam</h3>
    <p>Lorem ipsum dolor sit amet, consectetuer adipiscing elit sed diam nonummy nibh euismod tincid ut laoreet dolore magna aliquam erat volutpat, quis nostrud exerci tation ullamcorper suscipit lobortis nisl ut aliquip ex</p>
  </div>
  <div class="feature">
    <svg width="38" height="34" viewBox="0 0 38 34" fill="none" stroke="var(--blue)" stroke-width="2"><polyline points="2,4 8,4 12,22 30,22 34,9 10,9"/><circle cx="14" cy="28" r="2.5"/><circle cx="28" cy="28" r="2.5"/></svg>
    <h3>Dolore magna aliquam</h3>
    <p>Lorem ipsum dolor sit amet, consectetuer adipiscing elit sed diam nonummy nibh euismod tincid ut laoreet dolore magna aliquam erat volutpat. Ut wisi enim ad minim veniam, quis nostrud exerci tation ullamcorper suscipit</p>
  </div>
  <div class="feature">
    <svg width="38" height="34" viewBox="0 0 38 34" fill="none" stroke="var(--blue)" stroke-width="2"><path d="M3 4h20v13H11l-5 4v-4H3z"/><path d="M27 11h8v13h-3v4l-5-4H15v-4"/></svg>
    <h3>Dolore magna aliquam</h3>
    <p>Lorem ipsum dolor sit amet, consectetuer adipiscing elit sed diam nonummy nibh euismod tincid ut laoreet dolore magna aliquam erat volutpat. Ut wisi enim ad minim veniam, quis nostrud exerci tation ullamcorper suscipit</p>
  </div>
</section>

<section class="why">
  <div class="art" role="img" aria-label="Illustration of a laptop showing call scorecards over a faint globe"></div>
  <div class="laptop" role="img" aria-label="Laptop screen with scorecard list"></div>
  <div class="accordion">
    <div class="acc-head open">Why Choose US <b>−</b></div>
    <div class="acc-body">Lorem ipsum dolor sit amet, consectetuer adipiscing elit sed diam nonummy nibh euismod tincid ut laoreet dolore magna aliquam erat volutpat. Ut wisi enim ad minim veniam, quis nostrud exerci tation ullamcorper suscipit lobortis nisl ut aliquip ex ea commodo consequat. Duis autem vel eum iriure dolor in hendrerit in vulputate velit esse molestie consequat.</div>
    <div class="acc-head">Powerful Mission <b>+</b></div>
    <div class="acc-head">Brilliant Vision <b>+</b></div>
  </div>
</section>

<section class="intro">
  <h2 class="section-title">UT WISI ENIM AD MINIM VENIAM</h2>
  <p class="lead">Here are many variations of passages of Lorem Ipsum available, but the majority have suffered alteration in some form by injected humour, or randomised words which don't</p>
</section>

<section class="tiles">
  <div class="tile">
    <svg viewBox="0 0 110 100" fill="none" stroke="#fff" stroke-width="3"><path d="M5 40l20-14 18 6 12-6 22 2 28 16"/><path d="M30 60l18 14 8-4 8 6 8-4 10 4 14-20"/><path d="M43 32l-16 16 8 6 16-12"/></svg>
    <span class="label">DUIS AUTEM VEL EUM</span>
  </div>
  <div class="tile pale">
    <svg viewBox="0 0 110 100" fill="none" stroke="#fff" stroke-width="3"><rect x="20" y="60" width="12" height="30"/><rect x="42" y="45" width="12" height="45"/><rect x="64" y="65" width="12" height="25"/><rect x="86" y="35" width="12" height="55"/><polyline points="20,40 45,20 68,40 94,12"/><circle cx="20" cy="40" r="4"/><circle cx="45" cy="20" r="4"/><circle cx="68" cy="40" r="4"/><circle cx="94" cy="12" r="4"/></svg>
    <span class="label">DUIS AUTEM VEL EUM</span>
  </div>
  <div class="tile">
    <svg viewBox="0 0 110 100" fill="none" stroke="#fff" stroke-width="3"><rect x="25" y="15" width="75" height="50"/><polyline points="35,52 50,38 62,46 88,25"/><rect x="5" y="45" width="35" height="40"/><line x1="12" y1="55" x2="33" y2="55"/><line x1="12" y1="65" x2="33" y2="65"/><line x1="12" y1="75" x2="33" y2="75"/><line x1="45" y1="85" x2="100" y2="85"/></svg>
    <span class="label">DUIS AUTEM VEL EUM</span>
  </div>
  <div class="tile pale">
    <svg viewBox="0 0 110 100" fill="none" stroke="#fff" stroke-width="3"><rect x="30" y="45" width="50" height="45"/><line x1="55" y1="45" x2="55" y2="90"/><rect x="48" y="5" width="14" height="40"/><line x1="30" y1="60" x2="80" y2="60"/></svg>
    <span class="label">DUIS AUTEM VEL EUM</span>
  </div>
</section>

<section class="newsletter">
  <h4>JOIN OUT LATEST NEWSLETTER</h4>
  <span class="btn">SUBSCRIBE NOW</span>
</section>

<section class="pricing">
  <h2 class="section-title">PRICING</h2>
  <p class="lead">Here are many variations of passages of Lorem Ipsum available, but the majority have suffered alteration in some form by injected humour, or randomised words which don't</p>
  <div class="plans">
    <div class="plan">
      <div class="ribbon">PRICE 1</div>
      <p class="price"><sup>$</sup>12<small>/MO</small></p><div class="bar"></div>
      <ul><li>4 Free Websites</li><li>2 GB Storage</li><li>Unlimited Designs</li><li>Domain Name Included</li><li>200 BG Email</li><li>Unlimited Lifetime Support</li></ul>
      <span class="btn">CHOOSE PLAN</span>
    </div>
    <div class="plan featured">
      <div class="ribbon">PRICE 2</div>
      <p class="price"><sup>$</sup>59<small>/MO</small></p><div class="bar"></div>
      <ul><li>6 Free Websites</li><li>2 GB Storage</li><li>Unlimited Designs</li><li>Domain Name Included</li><li>200 BG Email</li><li>Unlimited Lifetime Support</li></ul>
      <span class="btn">CHOOSE PLAN</span>
    </div>
    <div class="plan">
      <div class="ribbon">PRICE 3</div>
      <p class="price"><sup>$</sup>79<small>/MO</small></p><div class="bar"></div>
      <ul><li>8 Free Websites</li><li>2 GB Storage</li><li>Unlimited Designs</li><li>Domain Name Included</li><li>200 BG Email</li><li>Unlimited Lifetime Support</li></ul>
      <span class="btn">CHOOSE PLAN</span>
    </div>
  </div>
</section>

<section class="video">
  <div class="copy">
    <h2>WATCH OUR VIDEO</h2>
    <p>Here are many variations of passages of Lorem Ipsum available, but the majority have suffered alteration in some form by injected humour, or randomised words which don't look even slightly believable. If you are going to use a passage of lorem Ipsum.</p>
    <p style="margin-top:14px">Here are many variations of passages of Lorem Ipsum available, but the majority have suffered alteration in</p>
    <span class="btn">MORE INFO</span>
  </div>
  <div class="player">
    <div class="screen" role="img" aria-label="Illustrated laptop showing the product video"></div>
    <div class="play"></div>
  </div>
</section>

<section class="team">
  <h2 class="section-title">CREATIVE TEAM</h2>
  <p class="lead">Here are many variations of passages of Lorem Ipsum available, but the majority have suffered alteration in some form by injected humour, or randomised words which don't</p>
  <span class="arrow" style="left:196px"></span><span class="arrow" style="left:982px"></span>
  <div class="members">
    <div class="member"><div class="photo" role="img" aria-label="Portrait photo of team member John Doe"></div><h4>John Doe</h4><span>POSITION</span></div>
    <div class="member active"><div class="photo" role="img" aria-label="Portrait photo of team member John Doe 2 with social links"><i></i><i></i><i></i></div><h4>John Doe 2</h4><span>POSITION</span></div>
    <div class="member"><div class="photo" role="img" aria-label="Portrait photo of team member Juan Doe"></div><h4>Juan Doe</h4><span>POSITION</span></div>
  </div>
</section>

<footer class="site-footer">
  <div class="brand"><span class="dot"></span>DialMetric</div>
  <ul class="contact"><li>123x Address here</li><li>(000) 123-0000</li><li>contact@dialmetric.com</li></ul>
  <div class="fcol" style="left:484px">
    <h4>SITE LINKS</h4>
    <ul class="links"><li>About Us</li><li>Services</li><li>Projects</li><li>Blog</li><li>Contact Us</li></ul>
  </div>
  <div class="fcol" style="left:795px">
    <h4>RECENT POSTS</h4>
    <div class="post"><i></i><div><b>WEBSITE POST WITH A SMART DESIGNED GALLERY</b><small>28 June 2016</small></div></div>
    <div class="post"><i></i><div><b>APPLICATION POST WITH A SMART DESIGNED GALLERY</b><small>21 June 2016</small></div></div>
  </div>
  <div class="copyright">© COPYRIGHT DIALMETRIC. ALL RIGHTS RESERVED<span><i></i><i></i><i></i></span></div>
</footer>

</body>
</html>
```